Kestin Power Battery advertisment for Facebook ads

Objective:
Design a compelling Facebook advertisement to promote the new Federal Government Home Battery Subsidy, encouraging existing solar customers to act now and install a battery system under the new subsidy program.

Key Message:

25kWh Battery System Installed from $9,800
Act now and secure your affordable energy future today!
Design Requirements:

Bold headline showcasing the 25kWh for $9,800 offer.
Clear reference to the Federal Government Battery Subsidy as the reason for the low pricing.
Include messaging around:
Claim your subsidy before it winds down—like the solar rebate, it reduces each year
The subsidy can only be claimed once per household—go large now to future-proof your energy needs
Add a strong Call to Action like: “Beat the Rush—Secure Your Battery Today!”

Target Market(s)

Home owners who want to add batteries to existing solar systems

Industry/Entity Type

Renewable energy

Colors
0054AA
0677BA
7BADD7
CADEEF
E8F1F8
EB3D1F
EC4F4E
F09395
F8D3D4
FCEDEE

Requirements
Must have
• Visual Style: Modern, clean, and high-trust Use imagery of solar homes, battery units, or families enjoying power security at night Include visual cues of savings, energy independence, or clean energy Mobile-optimized, designed for Facebook feed
Nice to have
• Tone: Confident, future-focused, and urgent—while remaining trustworthy and informative. I would like a picture of battery ideally VOM battery on a home or such
Should not have
• must be professional and be a call to action

```html
<!DOCTYPE html>
<html lang="en">
<head>
<meta charset="utf-8">
<title>Kestin Power – 25kWh Battery System Offer</title>
<link rel="stylesheet" href="https://fonts.googleapis.com/css2?family=Anton&family=Montserrat:ital,wght@0,800;1,700;1,800;1,900&display=swap">
<style>
  :root {
    --navy: #0a0f5c;
    --navy-deep: #050a4a;
    --blue: #0054aa;
    --violet: #6b6cf4;
    --green: #0a8a2a;
    --green-bright: #129a1e;
    --red: #eb1f1f;
    --white: #ffffff;
    --panel-grey: #e4e4e6;
    --ink: #111111;
  }
  * { margin: 0; padding: 0; box-sizing: border-box; }
  html, body { width: 1200px; height: 988px; overflow: hidden; background: var(--white); }
  .ad { position: relative; width: 1200px; height: 988px; overflow: hidden; font-family: "Montserrat", sans-serif; }
  .backdrop { position: absolute; inset: 0; }

  .headline-tile {
    position: absolute; display: flex; align-items: center; justify-content: center;
    font-family: "Anton", sans-serif; color: var(--white); font-style: italic;
    transform: rotate(-8deg) skewX(-10deg);
  }
  .tile-capacity {
    left: 124px; top: 118px; width: 236px; height: 118px;
    background: linear-gradient(135deg, var(--green) 0%, #0b4f48 55%, var(--navy) 100%);
    font-size: 80px;
  }
  .tile-capacity span, .tile-price span, .band-installed span { letter-spacing: -1px; }
  .word-battery {
    position: absolute; left: 386px; top: 80px;
    font-family: "Anton", sans-serif; font-size: 92px; color: var(--red);
    -webkit-text-stroke: 3px var(--white); paint-order: stroke fill;
    transform: rotate(-8deg) skewX(-12deg); letter-spacing: -1px;
  }
  .band-installed {
    left: 80px; top: 232px; width: 600px; height: 128px;
    background: linear-gradient(90deg, #050a2e 0%, var(--navy) 45%, #141a8a 100%);
    font-size: 88px;
  }
  .word-from {
    position: absolute; left: 258px; top: 378px;
    font-family: "Anton", sans-serif; font-size: 58px; color: var(--red);
    -webkit-text-stroke: 2px var(--white); paint-order: stroke fill;
    transform: rotate(-8deg) skewX(-12deg);
  }
  .tile-price {
    left: 402px; top: 352px; width: 222px; height: 114px;
    background: linear-gradient(135deg, var(--green-bright) 0%, #0b5a45 55%, var(--navy) 100%);
    font-size: 80px;
  }
  .rule { position: absolute; height: 2px; background: var(--white); transform: rotate(-8deg); }

  .icon-badge { position: absolute; border-radius: 50%; background: linear-gradient(160deg, #0a5a8a 0%, var(--green) 70%); display: flex; align-items: center; justify-content: center; }

  .pitch {
    position: absolute; left: 58px; top: 610px;
    font-weight: 800; font-size: 37px; line-height: 51px; color: var(--white);
    text-transform: uppercase; text-shadow: 0 2px 4px rgba(0,0,0,.35);
  }
  .subsidy-notes {
    position: absolute; left: 711px; top: 764px; width: 455px;
    font-size: 15px; line-height: 21.6px; font-weight: 900; font-style: italic; color: var(--ink);
  }
  .subsidy-notes .line { display: block; white-space: nowrap; }
  .subsidy-notes .justified { text-align: justify; text-align-last: justify; white-space: normal; }
  .subsidy-notes .spaced { letter-spacing: 1.6px; }
  .cta-bar {
    position: absolute; left: 0; top: 872px; width: 1200px; height: 116px;
    background: linear-gradient(90deg, var(--navy-deep) 0%, #1a2bb0 55%, var(--violet) 100%);
    display: flex; align-items: center; justify-content: center;
  }
  .cta-bar h2 { font-weight: 900; font-style: italic; font-size: 71px; color: var(--white); letter-spacing: .5px; white-space: nowrap; }
</style>
</head>
<body>
<main class="ad">
  <svg class="backdrop" width="1200" height="988" viewBox="0 0 1200 988">
    <defs>
      <linearGradient id="sky" x1="0" y1="0" x2="1" y2="1">
        <stop offset="0" stop-color="#d8dde6"/>
        <stop offset=".45" stop-color="#b99a7c"/>
        <stop offset=".75" stop-color="#8aa7d8"/>
        <stop offset="1" stop-color="#3f8de8"/>
      </linearGradient>
      <linearGradient id="navyField" x1="0" y1="0" x2="0" y2="1">
        <stop offset="0" stop-color="#9da2d2"/>
        <stop offset=".35" stop-color="#2a2f8f"/>
        <stop offset="1" stop-color="#080c5a"/>
      </linearGradient>
      <linearGradient id="haze" x1="0" y1="0" x2="1" y2="0">
        <stop offset="0" stop-color="#ffffff" stop-opacity=".7"/>
        <stop offset=".5" stop-color="#ffffff" stop-opacity="0"/>
      </linearGradient>
    </defs>
    <rect class="house-photo" role="img" aria-label="Photo of a suburban house with rooftop solar panels under a blue sky" width="1200" height="620" fill="url(#sky)"/>
    <rect width="1200" height="620" fill="url(#haze)"/>
    <path d="M0 470 Q320 600 700 555 Q880 530 1000 470 L1000 880 L0 880 Z" fill="url(#navyField)"/>
    <path d="M0 500 Q320 610 720 565" fill="none" stroke="#ffffff" stroke-opacity=".35" stroke-width="3"/>
    <path d="M680 880 Q620 560 900 340 Q1050 260 1200 250 L1200 880 Z" fill="var(--panel-grey)"/>
    <rect class="battery-photo" role="img" aria-label="Two white stacked home battery units with green status rings" x="808" y="288" width="370" height="468" rx="6" fill="#f2f2f3"/>
    <circle cx="777" cy="293" r="31" fill="#0a9a1a"/>
    <circle cx="707" cy="343" r="15" fill="#0a9a1a"/>
    <circle cx="728" cy="409" r="15" fill="#0a9a1a"/>
  </svg>

  <div class="headline-tile tile-capacity"><span>25kWh</span></div>
  <div class="word-battery">BATTERY</div>
  <div class="rule" style="left:356px;top:186px;width:332px"></div>
  <div class="headline-tile band-installed"><span>SYSTEM INSTALLED</span></div>
  <div class="word-from">FROM</div>
  <div class="rule" style="left:232px;top:444px;width:170px"></div>
  <div class="rule" style="left:262px;top:452px;width:140px"></div>
  <div class="headline-tile tile-price"><span>$9,800</span></div>

  <div class="icon-badge" style="left:614px;top:420px;width:80px;height:80px">
    <svg width="56" height="56" viewBox="0 0 56 56" fill="none" stroke="#fff" stroke-width="2.5">
      <path d="M10 22 A19 19 0 0 1 44 16"/><path d="M46 34 A19 19 0 0 1 12 40"/>
      <path d="M40 10 L44 16 L37 18"/><path d="M16 46 L12 40 L19 38"/>
      <path d="M31 12 L21 30 H29 L25 44 L36 25 H28 Z" fill="#fff" stroke="none"/>
    </svg>
  </div>
  <div class="icon-badge" style="left:582px;top:540px;width:134px;height:134px">
    <svg width="96" height="96" viewBox="0 0 96 96" fill="none" stroke="#fff" stroke-width="3">
      <path d="M40 18 A34 34 0 1 0 70 78"/>
      <path d="M58 16 Q80 6 82 -2 Q84 22 62 28 Q52 30 58 16 Z" transform="translate(-4 14)" fill="#fff" stroke="none"/>
      <rect x="62" y="72" width="18" height="14" rx="3" fill="#fff" stroke="none"/>
      <path d="M80 76 H88 M80 82 H88" stroke-width="3"/>
    </svg>
  </div>
  <div class="icon-badge" style="left:499px;top:692px;width:162px;height:162px">
    <svg width="100" height="90" viewBox="0 0 100 90">
      <path d="M50 6 L96 46 L88 54 L50 20 L12 54 L4 46 Z" fill="#fff"/>
      <rect x="74" y="12" width="10" height="20" fill="#fff"/>
      <path d="M20 48 L50 22 L80 48 V86 H58 V62 H42 V86 H20 Z" fill="#fff"/>
    </svg>
  </div>

  <p class="pitch">Act now and secure<br>your affordable<br>energy future<br>today!</p>

  <p class="subsidy-notes">
    <span class="line justified spaced">Claim your subsidy before it winds down</span>
    <span class="line justified spaced">like the solar rebate, it reduces each year</span>
    <span class="line justified">The subsidy can only be claimed once per household</span>
    <span class="line">go large now to future-proof your energy needs</span>
  </p>

  <footer class="cta-bar"><h2>Secure Your Battery Today!</h2></footer>
</main>
</body>
</html>
```